Etiketten-Design für Weinflasche
Sehr gute Zusammenarbeit bei Tag und Nacht, sehr kooperativ ,flexibel und entgegenkommend. Empfehlenswert
Zielgruppe
Weinbau - Eigenbau Wein -Weinverkauf
Aufgabenstellung
Bräuchte oder Suche ein Flaschenetikette für Rotwein der Marke Zweigelt Das Ausmaß der Etikette sollte 8cm Breit und 12cm Hoch sein. Habe meine letzte Etikette beigelegt sie Anhang

```html
<!DOCTYPE html>
<html lang="de">
<head>
<meta charset="utf-8">
<title>Zweigelt 2020 – Etiketten</title>
<link rel="stylesheet" href="https://fonts.googleapis.com/css2?family=Questrial&display=swap">
<style>
  :root {
    --backdrop: #999999;
    --band: #000000;
    --field-dark: #8c8c8c;
    --field-light: #bdbdbd;
    --back-label: #bdbdbd;
    --ink: #000000;
    --paper: #ffffff;
  }
  * { margin: 0; padding: 0; box-sizing: border-box; }
  html, body { width: 900px; height: 1200px; overflow: hidden; }
  body {
    background: var(--backdrop);
    font-family: "Questrial", "Century Gothic", sans-serif;
    color: var(--ink);
    position: relative;
  }
  .line {
    position: absolute;
    left: 0; right: 0;
    text-align: center;
    line-height: 1;
    white-space: nowrap;
    font-weight: 400;
  }

  /* Front label */
  .front-label {
    position: absolute;
    left: 78px; top: 348px;
    width: 342px; height: 513px;
    overflow: hidden;
  }
  .front-label .title-band {
    position: absolute;
    left: 0; top: 0; width: 100%; height: 151px;
    background: var(--band);
    color: var(--paper);
  }
  .front-label .vintage { top: 35px; font-size: 37px; }
  .front-label .variety { top: 70px; font-size: 74px; letter-spacing: -1px; }
  .front-label .field {
    position: absolute;
    left: 0; top: 151px; width: 100%; height: 362px;
  }
  .front-label .estate-mark { top: 282px; font-size: 34px; }
  .front-label .grower { top: 437px; font-size: 27px; }

  /* Back label */
  .back-label {
    position: absolute;
    left: 507px; top: 472px;
    width: 257px; height: 321px;
    background: var(--back-label);
  }
  .back-label .vintage { top: 25px; font-size: 26px; }
  .back-label .variety { top: 51px; font-size: 44px; letter-spacing: -0.5px; }
  .back-label .quality { top: 97px; font-size: 11px; }
  .back-label .lot { top: 111px; font-size: 11px; }
  .back-label .specs { top: 143px; font-size: 16px; }
  .back-label .region { top: 181px; font-size: 26px; }
  .back-label .bottler { top: 231px; font-size: 11px; }
  .back-label .producer { top: 245px; font-size: 16px; }
  .back-label .address { top: 262px; font-size: 12px; }
  .back-label .contact { top: 276px; font-size: 11px; }
  .back-label .allergen {
    top: 303px; left: auto; right: 16px; font-size: 9px; text-align: right;
  }
</style>
</head>
<body>
  <section class="front-label">
    <div class="title-band">
      <p class="line vintage">2020</p>
      <h1 class="line variety">Zweigelt</h1>
    </div>
    <svg class="field" viewBox="0 0 342 362" preserveAspectRatio="none">
      <rect width="342" height="362" fill="var(--field-light)"/>
      <polygon points="0,0 342,0 0,362" fill="var(--field-dark)"/>
    </svg>
    <p class="line estate-mark">Lomander</p>
    <p class="line grower">Tobias Lomander</p>
  </section>

  <section class="back-label">
    <p class="line vintage">2020</p>
    <h2 class="line variety">Zweigelt</h2>
    <p class="line quality">Österreichischer Qualitätswein</p>
    <p class="line lot">LE 4673/15</p>
    <p class="line specs">alc.14% vol. . trocken . 0,75 l</p>
    <p class="line region">Burgenland</p>
    <p class="line bottler">Erzeugerabfüllung</p>
    <p class="line producer">Weinbau Tobias Lomander</p>
    <p class="line address">A-7000 Rebenau, Kellergasse 8</p>
    <p class="line contact">Tel.: 0699/12 34 56 78 . t.lomander@netzpost.at</p>
    <p class="line allergen">enthält Sulfite</p>
  </section>
</body>
</html>
```